Business card design needed

Business Card design required for new small plumbing business.
Would like a logo/text look that is simple and unique and does not have to be representative of a plumbing company (ie. having a cartoon plumber or toilet etc) as the companyname is self explanatory.
Would like the main colour to be green (lime green).
Updates

Industry/Entity Type

Plumber

Contact Information for Business Card

BRAVELL PLUMBING
ABN 61 904 127 558 003

Trevor Hasketh
Licensed Plumber 83615
Phone: 0412 870 245

27 Bravell Drive,
Carrowby. 3987 Westmere

Email: bravellplumbing@mailnest.example

Logo Text

Bravell Plumbing

Logo styles of interest
Character Logo
Wordmark Logo
Lettermark Logo

```html
<!DOCTYPE html>
<html lang="en">
<head>
<meta charset="utf-8">
<title>Bravell Plumbing – Business Card</title>
<link rel="stylesheet" href="https://fonts.googleapis.com/css2?family=Source+Sans+3:wght@400;600;700&display=swap">
<style>
  :root {
    --lime: #b5d767;
    --slate: #6b7565;
    --border: #c4c4c4;
    --page: #ffffff;
  }
  * { margin: 0; padding: 0; box-sizing: border-box; }
  html, body {
    width: 1200px;
    height: 559px;
    overflow: hidden;
    background: var(--page);
    font-family: "Source Sans 3", "Myriad Pro", Arial, sans-serif;
  }
  .canvas { position: relative; width: 1200px; height: 559px; }

  .card {
    position: absolute;
    top: 125px;
    width: 534px;
    height: 309px;
    border: 1px solid var(--border);
    background: var(--page);
    overflow: hidden;
  }
  .card--front { left: 53px; }
  .card--back { left: 619px; }

  /* Front */
  .front-mark {
    position: absolute;
    left: 117px;
    top: 104px;
    width: 30px;
    height: 30px;
    background: var(--lime);
  }
  .front-name {
    position: absolute;
    left: 156px;
    top: 135px;
    font-size: 31px;
    font-weight: 600;
    letter-spacing: -0.6px;
    color: var(--slate);
    line-height: 1;
    white-space: nowrap;
  }
  .front-address {
    position: absolute;
    left: 156px;
    top: 171px;
    font-size: 15px;
    color: var(--slate);
    white-space: nowrap;
  }

  /* Back */
  .brand-panel {
    position: absolute;
    left: 0; top: 0;
    width: 175px;
    height: 100%;
    background: var(--slate);
  }
  .brand-panel__mark {
    position: absolute;
    left: 32px;
    top: 42px;
    width: 26px;
    height: 26px;
    background: var(--lime);
  }
  .brand-panel__name {
    position: absolute;
    left: 31px;
    top: 89px;
    font-size: 14px;
    font-weight: 700;
    letter-spacing: -0.4px;
    color: var(--lime);
    white-space: nowrap;
  }
  .contact-panel {
    position: absolute;
    left: 175px; top: 0;
    width: 277px;
    height: 100%;
    background: var(--lime);
    color: var(--slate);
  }
  .contact-panel__person {
    position: absolute;
    left: 14px;
    top: 78px;
    font-size: 26px;
    font-weight: 700;
    white-space: nowrap;
  }
  .contact-panel__role {
    position: absolute;
    left: 14px;
    top: 110px;
    font-size: 14px;
    white-space: nowrap;
  }
  .contact-panel__lines {
    position: absolute;
    left: 14px;
    top: 144px;
    font-size: 15.5px;
    font-weight: 700;
    line-height: 19px;
    white-space: nowrap;
  }
  .contact-panel__email { font-size: 14.5px; }
  .contact-panel__business {
    position: absolute;
    left: 14px;
    top: 242px;
    font-size: 14px;
    line-height: 17px;
    white-space: nowrap;
  }
  .contact-panel__abn { font-weight: 700; }
</style>
</head>
<body>
<main class="canvas">
  <section class="card card--front" aria-label="Business card front">
    <div class="front-mark"></div>
    <div class="front-name">BRAVELL PLUMBING</div>
    <div class="front-address">Bravell Drive, Carrowby. 3987 Westmere</div>
  </section>

  <section class="card card--back" aria-label="Business card back">
    <div class="brand-panel">
      <div class="brand-panel__mark"></div>
      <div class="brand-panel__name">BRAVELL PLUMBING</div>
    </div>
    <div class="contact-panel">
      <div class="contact-panel__person">Trevor Hasketh</div>
      <div class="contact-panel__role">- Licensed Plumber</div>
      <div class="contact-panel__lines">
        <div>0412 870 245 51 83615</div>
        <div class="contact-panel__email">bravellplumbing@mailnest.example</div>
      </div>
      <div class="contact-panel__business">
        <div class="contact-panel__abn">ABN 61 904 127 558 003</div>
        <div>Bravell Drive, Carrowby. 3987 Westmere</div>
      </div>
    </div>
  </section>
</main>
</body>
</html>
```